Bright Harbor Property Institute

This must be done in word press and I will need about 7 tabs The home page, Information page, Schedule and Cost page which will link to a Email me form, a online registration a about us and location/contact tab Each tab will then open several other pages. The home page will describe different courses that we offer since all the schools are about the same you can get a good ideal by going to plomvex.example or keelwardhomeclasses.example and looking at their site I would like mine to be similar as the courses are exactly the same but I would like the site to be more modern I also need it to be in word press so I can change it and update the dates as they change I have attached he logo below

Target Market(s)

people interested in getting into real estate and those who need continuing education

Coding

Number of Pages Required

Font styles to use
Sans Serif

Colors
3276b5

Requirements
Must have
• A page to schedule classes, a tab so the college I am partnering with can link the online courses to the back side, a page that describes the type of classes I offer

```html
<!DOCTYPE html>
<html lang="en">
<head>
<meta charset="utf-8">
<title>Bright Harbor Property Institute</title>
<link href="https://fonts.googleapis.com/css2?family=Poppins:ital,wght@0,400;0,500;0,600;0,700;0,800;1,400&display=swap" rel="stylesheet">
<style>
:root{
  --blue:#2f74b8;
  --blue-deep:#1a5fa8;
  --ink:#111;
  --muted:#666;
  --card:#e9f5fd;
  --footer:#1f1f1f;
  --footer-text:#cfcfcf;
  --grey-band:#5a5b5d;
}
*{box-sizing:border-box;margin:0;padding:0}
html,body{width:688px;height:1200px;overflow:hidden}
body{font-family:'Poppins',sans-serif;background:#fff;color:var(--ink);position:relative}

/* header */
.site-header{position:absolute;left:0;top:0;width:688px;height:35px;background:#fff}
.brand{position:absolute;left:71px;top:10px;display:flex;align-items:center;gap:3px;color:var(--blue);font-weight:700}
.brand-dot{width:8px;height:8px;border-radius:50%;background:var(--blue);flex:none}
.brand-name{font-size:5.2px;line-height:6px;letter-spacing:.2px;white-space:nowrap}
.search{position:absolute;left:151px;top:10px;width:111px;height:15px;background:#f1f1f1;border-radius:2px;font-size:5px;color:#888;padding:4.5px 6px}
.search svg{position:absolute;right:6px;top:4px}
.nav{position:absolute;left:296px;top:15px;display:flex;gap:8px;font-size:5px;font-weight:600;color:#222}
.nav .active{color:var(--blue)}
.signup{position:absolute;left:567px;top:12px;width:40px;height:12px;background:var(--blue);color:#fff;font-size:5px;font-weight:600;border-radius:2px;text-align:center;line-height:12px}

/* hero */
.hero{position:absolute;left:0;top:35px;width:688px;height:256px;background:linear-gradient(120deg,#d9d5cf 0%,#b7a89a 35%,#c98c6c 55%,#a99384 75%,#e6e3df 100%);overflow:hidden}
.hero-shape{position:absolute;left:0;top:0}
.hero-title{position:absolute;left:0;width:688px;top:93px;text-align:center;color:#fff;font-weight:800;font-size:30px;line-height:32px;letter-spacing:1px;text-shadow:0 1px 3px rgba(0,0,0,.25)}
.hero-sub{position:absolute;left:0;width:688px;top:132px;text-align:center;color:#fff;font-weight:700;font-size:15px;letter-spacing:.5px;text-shadow:0 1px 3px rgba(0,0,0,.3)}
.btn{position:absolute;background:var(--blue-deep);color:#fff;font-weight:600;text-align:center}
.hero .btn{left:303px;top:163px;width:83px;height:20px;line-height:20px;font-size:6px}

/* sections */
.section-title{position:absolute;left:0;width:688px;text-align:center;font-weight:600;font-size:13px;letter-spacing:.3px}
.divider{position:absolute;left:337px;width:14px;height:2px;border-top:.5px solid #555;border-bottom:.5px solid #555}

.card{position:absolute;width:133px;height:144px;background:var(--card);text-align:center}
.card svg{position:absolute;left:48px;top:16px}
.card h3{position:absolute;left:0;width:100%;top:61px;font-size:8.3px;font-weight:600}
.card p{position:absolute;left:11px;width:111px;top:81px;font-size:5.1px;line-height:8.6px;color:var(--muted)}
.card a{position:absolute;left:0;width:100%;top:124px;font-size:4.8px;font-weight:600;color:var(--blue);text-decoration:none}

/* cta */
.cta{position:absolute;left:0;top:703px;width:688px;height:96px;background:linear-gradient(100deg,#eef0f2 0%,#d7dadd 45%,#9ea3a9 75%,#dfe2e4 100%)}
.cta-text{position:absolute;left:179px;top:39px;font-size:18.5px;font-weight:700;color:#111}
.cta .btn{left:427px;top:38px;width:82px;height:20px;line-height:20px;font-size:6px}

/* testimonials */
.quote{position:absolute;width:133px;height:57px;border:.6px solid #999;background:#fff}
.quote-tip{position:absolute;left:62px;bottom:-4px;width:6px;height:6px;background:#fff;border-right:.6px solid #999;border-bottom:.6px solid #999;transform:rotate(45deg)}
.quote-mark{position:absolute;left:10px;top:14px;font-size:9px;font-weight:700;color:var(--blue);line-height:6px}
.quote p{position:absolute;left:25px;top:15px;width:102px;font-size:5.8px;line-height:8.6px;font-style:italic;font-weight:400;color:#333;letter-spacing:.2px}
.author{position:absolute;display:flex;align-items:center;gap:8px}
.avatar{width:18px;height:18px;background:linear-gradient(#8d8d8d,#4b4f57)}
.author b{display:block;font-size:6px;font-weight:600;color:var(--blue);letter-spacing:.3px;line-height:7px}
.author span{display:block;font-size:5px;color:#777;line-height:6px}

/* footer */
.footer{position:absolute;left:0;top:1003px;width:688px;height:197px;background:var(--footer);color:var(--footer-text)}
.footer .brand{left:134px;top:28px}
.footer .brand-name{font-size:9px;line-height:10px}
.footer .brand-dot{width:10px;height:10px}
.footer-about{position:absolute;left:134px;top:61px;width:134px;font-size:5px;line-height:8.6px}
.social{position:absolute;left:134px;top:124px;display:flex;gap:4px}
.social span{width:14px;height:14px;border:.7px solid #aaa;border-radius:50%}
.f-head{position:absolute;top:35px;font-size:6.2px;font-weight:600;color:#fff}
.f-links{position:absolute;left:290px;top:51px;list-style:none;font-size:5px}
.f-links li{height:12.9px;display:flex;align-items:center;gap:5px}
.f-links li::before{content:"";width:5px;height:.5px;background:#aaa}
.contact-row{position:absolute;left:365px;display:flex;gap:7px;font-size:5px;line-height:8.5px}
.c-icon{width:12px;height:12px;background:#3a3a3a;border-radius:1px;display:flex;align-items:center;justify-content:center;flex:none}
.news-text{position:absolute;left:457px;top:51px;width:100px;font-size:5px;line-height:8.5px}
.news-input{position:absolute;left:457px;top:74px;width:76px;height:18px;background:#fff;font-size:5px;color:#666;padding:6px 0 0 15px}
.news-btn{position:absolute;left:533px;top:74px;width:21px;height:18px;background:var(--blue);display:flex;align-items:center;justify-content:center}
.copyright{position:absolute;left:0;width:688px;top:183px;text-align:center;font-size:5px;color:#888}
</style>
</head>
<body>

<header class="site-header">
  <div class="brand"><span class="brand-dot"></span><span class="brand-name">BRIGHT HARBOR<br>PROPERTY INSTITUTE</span></div>
  <div class="search">Search for anything
    <svg width="6" height="6" viewBox="0 0 10 10"><circle cx="4" cy="4" r="3" fill="none" stroke="#666" stroke-width="1.2"/><path d="M6.3 6.3 9 9" stroke="#666" stroke-width="1.2"/></svg>
  </div>
  <nav class="nav">
    <span class="active">HOME</span><span>INFORMATION</span><span>SCHEDULE &amp; COST</span><span>REGISTRATION</span><span>ABOUT US</span><span>LOCATION</span><span>CONTACT</span>
  </nav>
  <div class="signup">Sign up</div>
</header>

<section class="hero" role="img" aria-label="Photo of an instructor presenting to students in a bright classroom">
  <svg class="hero-shape" width="688" height="256" viewBox="0 0 688 256">
    <polygon points="345,225 688,195 688,256" fill="var(--grey-band)"/>
    <polygon points="0,256 0,255 345,225 688,256" fill="#fff"/>
  </svg>
  <h1 class="hero-title">BRIGHT HARBOR</h1>
  <div class="hero-sub">PROPERTY INSTITUTE</div>
  <div class="btn">GET STARTED</div>
</section>

<h2 class="section-title" style="top:313px">Welcome to Bright Harbor Property Institute</h2>
<div class="divider" style="top:338px"></div>

<div class="card" style="left:134px;top:369px">
  <svg width="37" height="40" viewBox="0 0 37 40"><path d="M18.5 1 35 10v20L18.5 39 2 30V10z" fill="var(--blue)" stroke="var(--blue)" stroke-width="2" stroke-linejoin="round"/><circle cx="18.5" cy="20" r="10" fill="none" stroke="#fff" stroke-width="2"/><rect x="17.3" y="18" width="2.4" height="7" fill="#fff"/><circle cx="18.5" cy="15" r="1.5" fill="#fff"/></svg>
  <h3>Information</h3>
  <p>Lorem ipsum dolor sit amet, consectetur adipiscing elit. Mauris eget rutrum elit. Quisque at orci ut nunc blandit egestas. Pellentesque et purus odio.</p>
  <a href="#">LEARN MORE</a>
</div>
<div class="card" style="left:278px;top:369px">
  <svg width="37" height="40" viewBox="0 0 37 40"><path d="M18.5 1 35 10v20L18.5 39 2 30V10z" fill="var(--blue)" stroke="var(--blue)" stroke-width="2" stroke-linejoin="round"/><text x="18.5" y="27" text-anchor="middle" font-family="Poppins,sans-serif" font-weight="700" font-size="20" fill="#fff">$</text></svg>
  <h3>Schedule &amp; Cost</h3>
  <p>Lorem ipsum dolor sit amet, consectetur adipiscing elit. Mauris eget rutrum elit. Quisque at orci ut nunc blandit egestas. Pellentesque et purus odio.</p>
  <a href="#">LEARN MORE</a>
</div>
<div class="card" style="left:421px;top:369px">
  <svg width="37" height="40" viewBox="0 0 37 40"><path d="M18.5 1 35 10v20L18.5 39 2 30V10z" fill="var(--blue)" stroke="var(--blue)" stroke-width="2" stroke-linejoin="round"/><rect x="11" y="10" width="15" height="20" rx="1.5" fill="none" stroke="#fff" stroke-width="1.5"/><rect x="15" y="8" width="7" height="3.5" rx="1" fill="#fff"/><path d="M15 19l2.5 2.5L22 17" fill="none" stroke="#fff" stroke-width="1.5"/><path d="M14 26h9" stroke="#fff" stroke-width="1.2"/></svg>
  <h3>Registration</h3>
  <p>Lorem ipsum dolor sit amet, consectetur adipiscing elit. Mauris eget rutrum elit. Quisque at orci ut nunc blandit egestas. Pellentesque et purus odio.</p>
  <a href="#">LEARN MORE</a>
</div>
<div class="card" style="left:134px;top:523px">
  <svg width="37" height="40" viewBox="0 0 37 40"><path d="M18.5 1 35 10v20L18.5 39 2 30V10z" fill="var(--blue)" stroke="var(--blue)" stroke-width="2" stroke-linejoin="round"/><path d="M9 12h8v16H9zM17 12h8v10" fill="none" stroke="#fff" stroke-width="1.5"/><rect x="22" y="21" width="6" height="9" rx="3" fill="none" stroke="#fff" stroke-width="1.5"/></svg>
  <h3>Online Courses</h3>
  <p>Lorem ipsum dolor sit amet, consectetur adipiscing elit. Mauris eget rutrum elit. Quisque at orci ut nunc blandit egestas. Pellentesque et purus odio.</p>
  <a href="#">LEARN MORE</a>
</div>
<div class="card" style="left:278px;top:523px">
  <svg width="37" height="40" viewBox="0 0 37 40"><path d="M18.5 1 35 10v20L18.5 39 2 30V10z" fill="var(--blue)" stroke="var(--blue)" stroke-width="2" stroke-linejoin="round"/><circle cx="18.5" cy="20" r="10" fill="none" stroke="#fff" stroke-width="2"/><text x="18.5" y="24.5" text-anchor="middle" font-family="Poppins,sans-serif" font-weight="700" font-size="12" fill="#fff">?</text></svg>
  <h3>Why Bright Harbor?</h3>
  <p>Lorem ipsum dolor sit amet, consectetur adipiscing elit. Mauris eget rutrum elit. Quisque at orci ut nunc blandit egestas. Pellentesque et purus odio.</p>
  <a href="#">LEARN MORE</a>
</div>
<div class="card" style="left:421px;top:523px">
  <svg width="37" height="40" viewBox="0 0 37 40"><path d="M18.5 1 35 10v20L18.5 39 2 30V10z" fill="var(--blue)" stroke="var(--blue)" stroke-width="2" stroke-linejoin="round"/><path d="M10 20 22 10l6 6-12 12zM22 10l-5 11 11-5" fill="none" stroke="#fff" stroke-width="1.4" stroke-linejoin="round"/><path d="M8 27l3-3M10 30l3-3" stroke="#fff" stroke-width="1.2"/></svg>
  <h3>Get in Touch</h3>
  <p>Lorem ipsum dolor sit amet, consectetur adipiscing elit. Mauris eget rutrum elit. Quisque at orci ut nunc blandit egestas. Pellentesque et purus odio.</p>
  <a href="#">LEARN MORE</a>
</div>

<section class="cta" role="img" aria-label="Photo of a laptop keyboard and phone on a white desk">
  <div class="cta-text">Ready to Get Started?</div>
  <div class="btn">GET IN TOUCH</div>
</section>

<h2 class="section-title" style="top:830px">What Our Students Have To Say</h2>
<div class="divider" style="top:855px"></div>

<div class="quote" style="left:134px;top:877px"><span class="quote-mark">&ldquo;</span><p>Lorem ipsum dolor sit amet, consectetur adipiscing elit. Ut consectetur facilisis ultricies.</p><span class="quote-tip"></span></div>
<div class="quote" style="left:278px;top:877px"><span class="quote-mark">&ldquo;</span><p>Lorem ipsum dolor sit amet, consectetur adipiscing elit. Ut consectetur facilisis ultricies.</p><span class="quote-tip"></span></div>
<div class="quote" style="left:421px;top:877px"><span class="quote-mark">&ldquo;</span><p>Lorem ipsum dolor sit amet, consectetur adipiscing elit. Ut consectetur facilisis ultricies.</p><span class="quote-tip"></span></div>

<div class="author" style="left:172px;top:947px"><div class="avatar" role="img" aria-label="Student portrait"></div><div><b>John Smith</b><span>Client</span></div></div>
<div class="author" style="left:316px;top:947px"><div class="avatar" role="img" aria-label="Student portrait"></div><div><b>John Smith</b><span>Client</span></div></div>
<div class="author" style="left:459px;top:947px"><div class="avatar" role="img" aria-label="Student portrait"></div><div><b>John Smith</b><span>Client</span></div></div>

<footer class="footer">
  <div class="brand"><span class="brand-dot"></span><span class="brand-name">BRIGHT HARBOR<br>PROPERTY INSTITUTE</span></div>
  <p class="footer-about">Lorem ipsum dolor sit amet, consectetur adipiscing elit. Mauris eget rutrum elit. Quisque at orci ut nunc blandit egestas. Pellentesque et purus odio. Nulla ligula magna, vulputate sed elementum quis, vehicula quis enim. Nam eget sem tincidunt, tempus enim ultricies</p>
  <div class="social"><span></span><span></span><span></span><span></span></div>

  <div class="f-head" style="left:290px">QUICK LINKS</div>
  <ul class="f-links">
    <li>Home</li><li>Information</li><li>Schedule &amp; Cost</li><li>Registration</li><li>About Us</li><li>Location</li><li>Contact</li>
  </ul>

  <div class="f-head" style="left:366px">GET IN TOUCH</div>
  <div class="contact-row" style="top:52px"><span class="c-icon"><svg width="5" height="6" viewBox="0 0 10 12"><path d="M5 0a4 4 0 0 1 4 4c0 3-4 8-4 8S1 7 1 4a4 4 0 0 1 4-4z" fill="#ddd"/><circle cx="5" cy="4" r="1.5" fill="#3a3a3a"/></svg></span><span>218 Harbor Lane,<br>Port City - H204</span></div>
  <div class="contact-row" style="top:79px"><span class="c-icon"><svg width="6" height="6" viewBox="0 0 10 10"><path d="M2 0l2 2-1 2c1 1.5 2 2.5 3 3l2-1 2 2-2 2C4 10 0 6 0 2z" fill="#ddd"/></svg></span><span style="line-height:12px">555-014-2290</span></div>
  <div class="contact-row" style="top:98px"><span class="c-icon"><svg width="6" height="5" viewBox="0 0 10 8"><rect width="10" height="8" fill="#ddd"/><path d="M0 0l5 4 5-4" fill="none" stroke="#3a3a3a"/></svg></span><span style="line-height:12px">info@brightharbor.example</span></div>

  <div class="f-head" style="left:457px">NEWSLETTER</div>
  <p class="news-text">Enter your email to receive updates and specials</p>
  <div class="news-input">Email Address</div>
  <div class="news-btn"><svg width="8" height="8" viewBox="0 0 10 10"><path d="M0 4 10 0 7 10 5 6z" fill="#fff"/></svg></div>

  <div class="copyright">Copyright © 2019 Bright Harbor Property Institute. All Rights Reserved</div>
</footer>

</body>
</html>
```